Professional Business Cards

We need a nice looking, profession and modern business card for our new company. Our logo is attatched

Target Market(s)

Young Professionals

Industry/Entity Type

Financial

Contact Information for Business Card

FRONT

Vardane Ledger Pty Ltd
Level 22, Harbour Point, 48 Wattlebrook Ave
Sydney NSW 2000
ABN : 47 318 905 226

Owen Hadley - Chief Operations Officer
P : 02 9173 5528
M: 0418 356 091
owen@vardaneledger,com

BACK

- Cryptocurrency Exchange Services
- Cryptocurrency Mining Operations
- Cryptocurrency Investment Fund Offering

Font styles to use
Sans Serif

Colors
0255a3
9d9d9d

```html
<!DOCTYPE html>
<html lang="en">
<head>
<meta charset="utf-8">
<title>Vardane Ledger – Business Cards</title>
<link rel="stylesheet" href="https://fonts.googleapis.com/css2?family=Roboto+Condensed:wght@400;500;700&family=Saira+Semi+Condensed:wght@600;700&display=swap">
<style>
  :root {
    --brand-blue: #0255a3;
    --brand-blue-deep: #044a8f;
    --brand-grey: #9d9d9d;
    --band-grey: #6e6f71;
    --paper: #f2f2f2;
    --backdrop: #b9b9b9;
    --ink-light: #ffffff;
    --ink-soft: #dfe9f5;
  }
  * { box-sizing: border-box; margin: 0; padding: 0; }
  html, body { width: 1200px; height: 576px; overflow: hidden; }
  body {
    position: relative;
    background: var(--backdrop);
    font-family: "Roboto Condensed", "Arial Narrow", sans-serif;
  }
  .card {
    position: absolute;
    top: 138px;
    height: 294px;
    overflow: hidden;
    box-shadow: 0 3px 8px rgba(0,0,0,0.25);
  }

  /* Back side – services */
  .card--services {
    left: 81px;
    width: 486px;
    background: linear-gradient(135deg, #0a5fad 0%, var(--brand-blue) 45%, var(--brand-blue-deep) 100%);
  }
  .wordmark {
    position: absolute;
    left: 0; right: 0;
    top: 92px;
    display: flex;
    align-items: center;
    justify-content: center;
    gap: 14px;
  }
  .wordmark__square {
    width: 34px; height: 34px;
    background: var(--ink-light);
  }
  .wordmark__name {
    color: var(--ink-light);
    font-weight: 700;
    font-size: 40px;
    letter-spacing: 1px;
    text-transform: uppercase;
    line-height: 1;
  }
  .services {
    position: absolute;
    left: 0; right: 0;
    top: 216px;
    list-style: none;
  }
  .services__item {
    position: relative;
    height: 15.5px;
    display: flex;
    align-items: center;
    justify-content: center;
    gap: 8px;
    color: var(--ink-light);
    font-size: 12.5px;
    font-weight: 500;
  }
  .services__item::before {
    content: "";
    position: absolute;
    left: 0; right: 0; top: 50%;
    height: 1px;
    background: rgba(120,180,240,0.35);
    z-index: 0;
  }
  .services__item span, .services__item i { position: relative; z-index: 1; }
  .services__item i {
    width: 6px; height: 6px;
    border: 1px solid #5fa3e6;
    background: var(--brand-blue);
    transform: rotate(45deg);
  }

  /* Front side – contact */
  .card--contact {
    left: 602px;
    width: 481px;
    background: var(--paper);
  }
  .card--contact .panel {
    position: absolute;
    inset: 0;
    width: 100%;
    height: 100%;
  }
  .person {
    position: absolute;
    left: 20px; top: 24px;
    color: var(--ink-light);
  }
  .person__name {
    font-family: "Saira Semi Condensed", "Roboto Condensed", sans-serif;
    font-weight: 700;
    font-size: 21px;
    letter-spacing: 1px;
    text-transform: uppercase;
    line-height: 1.1;
  }
  .person__title {
    font-size: 10px;
    color: var(--ink-soft);
    margin-top: 3px;
  }
  .contacts {
    position: absolute;
    left: 20px; top: 71px;
    list-style: none;
    color: var(--ink-light);
    font-size: 12px;
  }
  .contacts li {
    display: flex;
    align-items: center;
    gap: 9px;
    height: 15.5px;
  }
  .contacts svg { width: 10px; height: 10px; fill: var(--ink-light); }
  .company-band {
    position: absolute;
    left: 0; top: 191px;
    width: 268px; height: 29px;
    background: var(--band-grey);
    color: var(--ink-light);
    font-weight: 700;
    font-size: 17px;
    letter-spacing: 0.5px;
    text-transform: uppercase;
    padding-left: 20px;
    line-height: 29px;
  }
  .company-details {
    position: absolute;
    left: 20px; top: 227px;
    color: var(--ink-light);
    font-size: 11.5px;
    line-height: 15px;
  }
  .wordmark--vertical {
    position: absolute;
    left: 395px; top: 146px;
    transform: translate(-50%, -50%) rotate(-90deg);
    display: flex;
    align-items: center;
    gap: 10px;
    white-space: nowrap;
  }
  .wordmark--vertical .wordmark__name {
    color: var(--brand-blue);
    font-size: 26px;
  }
  .wordmark--vertical .wordmark__square {
    width: 20px; height: 20px;
    background: var(--brand-blue);
  }
</style>
</head>
<body>

<section class="card card--services" aria-label="Card back: services">
  <div class="wordmark">
    <div class="wordmark__square"></div>
    <div class="wordmark__name">Vardane Ledger</div>
  </div>
  <ul class="services">
    <li class="services__item"><i></i><span>Cryptocurrency Exchange Services</span><i></i></li>
    <li class="services__item"><i></i><span>Cryptocurrency Mining Operations</span><i></i></li>
    <li class="services__item"><i></i><span>Cryptocurrency Investment Fund Offering</span><i></i></li>
  </ul>
</section>

<section class="card card--contact" aria-label="Card front: contact">
  <svg class="panel" viewBox="0 0 481 294" preserveAspectRatio="none" aria-hidden="true">
    <path d="M0 0 H308 Q256 147 318 294 H0 Z" fill="#0255a3"/>
    <path d="M300 0 Q256 147 318 294 H312 Q268 150 312 6 Z" fill="#fff" opacity="0.9"/>
    <path d="M312 6 Q268 150 318 294 H326 Q276 150 314 4 Z" fill="#7a7b7d"/>
  </svg>

  <div class="person">
    <div class="person__name">Owen Hadley</div>
    <div class="person__title">Chief Operations Officer</div>
  </div>

  <ul class="contacts">
    <li><svg viewBox="0 0 10 10"><path d="M1 3 Q5 0 9 3 L8 4.5 6.5 4 V3.2 H3.5 V4 L2 4.5 Z M2.5 5 H7.5 L8.5 9 H1.5 Z"/></svg>02 9173 5528</li>
    <li><svg viewBox="0 0 10 10"><path d="M3 0.5 H7 V9.5 H3 Z M3.8 1.5 V7.5 H6.2 V1.5 Z"/></svg>0418 356 091</li>
    <li><svg viewBox="0 0 10 10"><path d="M0.5 2 H9.5 V8 H0.5 Z M1 2.5 L5 5.5 9 2.5" stroke="#0255a3" stroke-width="0.8"/></svg>owen@vardaneledger.com</li>
    <li><svg viewBox="0 0 10 10"><circle cx="5" cy="5" r="4.2"/><path d="M1 5 H9 M5 1 V9 M5 1 Q2.5 5 5 9 M5 1 Q7.5 5 5 9" stroke="#0255a3" stroke-width="0.7" fill="none"/></svg>www.vardaneledger.com</li>
  </ul>

  <div class="company-band">Vardane Ledger Pty Ltd</div>

  <div class="company-details">
    ABN : 47 318 905 226<br>
    Level 22, Harbour Point, 48 Wattlebrook<br>
    Ave, Sydney NSW 2000
  </div>

  <div class="wordmark wordmark--vertical">
    <div class="wordmark__square"></div>
    <div class="wordmark__name">Vardane Ledger</div>
  </div>
</section>

</body>
</html>
```